Insurance Agency website design for Halvern Crest Insurance, LP

Build a website for Halvern Crest Insurance, LP which sells Homeowners, Auto, Renters, Condo, Flood, Disability, Life, Umbrella, and health insurance. We need the coolest insurance agency website out there to get quotes, contact us, or get additional information. Please list the following insurance companies we work with: Corvalith, Velk, Meridale Union, Tarvix, Brookwynd, QZT, and Pellurian.

Target Market(s)

Make a design similar to https://www.fandelmora.example/

Industry/Entity Type

Selling personal insurance policies

Coding

Coded - Design and coding required

Number of Pages Required

3 page

```html
<!DOCTYPE html>
<html lang="en">
<head>
<meta charset="utf-8">
<title>Halvern Crest Insurance, LP</title>
<link rel="stylesheet" href="https://fonts.googleapis.com/css2?family=Roboto:wght@400;500;700&family=Lato:wght@400;700&display=swap">
<style>
:root{
  --navy:#0b2a86;
  --navy-dark:#07206e;
  --green:#6a9a35;
  --blue:#1f6fd2;
  --blue-light:#2d83e3;
  --ink:#222;
  --muted:#444;
  --pale:#f2f3f6;
  --white:#fff;
}
*{box-sizing:border-box;margin:0;padding:0}
html,body{width:1200px;height:3341px;overflow:hidden}
body{font-family:'Lato',sans-serif;color:var(--ink);background:var(--white);position:relative}
h1,h2,h3,h4,.btn,.nav a{font-family:'Roboto',sans-serif}
a{color:inherit;text-decoration:none}
.wrap{width:980px;margin:0 auto;position:relative}

.topbar{height:40px;background:var(--navy);color:var(--white);font-family:'Roboto',sans-serif;font-size:15px}
.topbar .wrap{display:flex;justify-content:space-between;align-items:center;height:40px;padding:0 5px}
.topbar b{font-weight:500}

.header{height:87px;background:var(--white)}
.header .wrap{display:flex;justify-content:space-between;align-items:center;height:87px}
.brand{display:flex;align-items:center;gap:10px}
.brand-mark{width:36px;height:36px;background:var(--green)}
.brand-name{font-family:'Roboto',sans-serif;font-weight:500;font-size:20px;line-height:1.3;color:var(--navy)}
.nav{display:flex;align-items:center;gap:40px;font-size:17px}
.nav .active{color:var(--green)}
.btn{display:inline-flex;align-items:center;gap:8px;font-weight:700;font-size:17px;color:var(--white);padding:0 22px;height:46px;border-radius:2px}
.btn-green{background:var(--green)}
.btn-navy{background:var(--navy)}

.hero{background:linear-gradient(180deg,var(--blue) 0%,var(--blue-light) 100%);height:673px;position:relative;color:var(--white);text-align:center}
.hero h1{font-size:48px;font-weight:700;line-height:56px;padding-top:80px}
.hero p{font-size:17px;line-height:31px;width:920px;margin:14px auto 0}
.hero-cards{position:absolute;top:337px;left:0;width:1200px;height:233px;display:flex}
.hcard{flex:1;display:flex;align-items:center;padding-left:58px;gap:20px}
.hcard.navy{background:var(--navy)}
.hcard.green{background:var(--green)}
.hcard .ring{width:156px;height:156px;border-radius:50%;border:2px solid var(--white);display:flex;align-items:center;justify-content:center;flex:none}
.hcard .ring div{width:140px;height:140px;border-radius:50%}
.hcard h3{font-size:25px;font-weight:500;margin-bottom:10px}
.hcard p{font-size:15.5px;line-height:30px;text-align:left;width:340px;margin:0}
.hcard .pill{margin-top:12px;height:42px;border-radius:21px;padding:0 30px;font-size:16px;font-weight:500;display:inline-flex;align-items:center;gap:10px}
.strip{position:absolute;bottom:0;left:0;width:1200px;height:50px;background:var(--navy-dark);font-size:15.5px;display:flex;align-items:center;justify-content:center;gap:6px}
.strip u{font-weight:700}

.partners{height:220px;display:flex;align-items:center;justify-content:center;position:relative}
.partners .row{display:flex;justify-content:space-between;align-items:center;width:970px;font-family:'Roboto',sans-serif;font-weight:700;font-size:27px;color:#1d1d1d}
.partners .arrow{position:absolute;top:98px}

.about{height:521px}
.about .wrap{display:flex;justify-content:space-between;padding-top:36px}
.about-text{width:470px;padding-top:22px}
h2.title{font-size:32px;font-weight:700;color:var(--navy)}
h2.title span{color:var(--green)}
.about-text p{font-size:15.5px;line-height:30px;margin-top:16px;color:var(--ink)}
.about-text p+p{margin-top:0}
.about-text .btn{margin-top:22px;height:46px}
.about-figure{position:relative;width:463px;height:370px}
.about-figure .back{position:absolute;right:0;top:0;width:262px;height:205px;background:var(--green)}
.about-figure .frame{position:absolute;left:0;top:19px;width:446px;height:349px;border:2px solid var(--navy);background:var(--white)}
.about-figure .photo{position:absolute;left:13px;top:9px;width:441px;height:345px;background:linear-gradient(135deg,#d9d3c8,#9fb1b8 60%,#c7b6a0)}

.info{background:var(--pale);height:782px;text-align:center;padding-top:76px}
.info h2{font-size:32px;font-weight:700;color:var(--navy)}
.info h2 span{color:var(--green)}
.info .sub{font-size:17px;margin-top:12px;color:var(--muted)}
.cards{display:flex;justify-content:space-between;width:980px;margin:24px auto 0}
.card{width:460px;height:448px;background:var(--white);border-radius:10px;box-shadow:0 2px 12px rgba(0,0,0,.15);padding:15px;position:relative}
.card.g{border-bottom:6px solid var(--green)}
.card.n{border-bottom:6px solid var(--navy)}
.card .img{height:218px;border-radius:8px}
.card h3{font-size:21px;font-weight:500;margin-top:26px;line-height:30px;color:#111}
.card p{font-size:15.5px;line-height:29px;color:var(--muted);margin-top:8px;padding:0 10px}
.card .more{display:block;margin-top:14px;font-family:'Roboto',sans-serif;font-weight:700;font-size:17px}
.card.g .more{color:var(--green)}
.card.n .more{color:var(--navy)}
.blog-link{display:inline-block;margin-top:44px;font-family:'Roboto',sans-serif;font-weight:700;font-size:19px;color:var(--navy)}

.quote{height:592px}
.quote .wrap{display:flex;justify-content:space-between;padding-top:88px}
.quote-form{width:450px;padding-left:4px}
.quote-form h3{font-size:23.5px;font-weight:500;line-height:37px;color:#111;width:450px}
.quote-form label{display:block;font-size:15.5px;color:var(--muted);margin-top:22px}
.field{display:flex;width:440px;height:50px;border:1px solid #ccc;margin-top:16px;margin-left:-2px}
.field .ico{width:46px;background:var(--pale);display:flex;align-items:center;justify-content:center;border-right:1px solid #ccc}
.field span{padding-left:20px;display:flex;align-items:center;font-size:14px;color:#333}
.quote-form .field+label{margin-top:26px}
.quote-form .btn{margin-top:28px;height:46px;padding:0 24px}
.quote-info{width:450px}
.quote-info p{font-size:15.5px;line-height:31px;margin-top:18px;color:var(--ink)}
.quote-info .btn{margin-top:22px}

.footer{background:var(--navy);height:426px;color:var(--white);position:relative}
.footer .cols{display:flex;width:985px;margin:0 auto;padding-top:65px}
.footer h4{font-size:22px;font-weight:500;margin-bottom:16px}
.footer ul{list-style:none;font-size:16px;line-height:31px}
.footer li{display:flex;align-items:center;gap:10px}
.contact-row{display:flex;align-items:center;gap:12px;font-size:16px;margin-bottom:24px}
.contact-row i{width:36px;height:36px;border-radius:50%;background:var(--green);display:flex;align-items:center;justify-content:center;flex:none}
.news p{font-size:15.5px;line-height:31px}
.news .email{margin-top:6px;border-bottom:2px solid var(--white);width:270px;padding:0 0 10px 2px;font-size:15px}
.news .sub-btn{margin-top:30px;width:146px;height:50px;border-radius:25px;background:var(--green);font-family:'Roboto',sans-serif;font-weight:700;font-size:18px;display:flex;align-items:center;justify-content:center;margin-left:6px}
.copyright{position:absolute;left:98px;right:98px;bottom:0;height:63px;border-top:1px solid rgba(255,255,255,.6);text-align:center;font-size:15px;padding-top:20px}
</style>
</head>
<body>

<div class="topbar">
  <div class="wrap">
    <span><b>For inquiries (555) 318-2740</b></span>
    <span>Are you an independent agent? <b>Sign Up</b> &nbsp;|&nbsp; <b>Log In</b></span>
  </div>
</div>

<header class="header">
  <div class="wrap">
    <div class="brand">
      <div class="brand-mark"></div>
      <div class="brand-name">Halvern Crest<br>Insurance, LP</div>
    </div>
    <nav class="nav">
      <a class="active" href="#">Home</a>
      <a href="#">About Us</a>
      <a href="#">Get a Quotes</a>
      <a class="btn btn-green" href="#">Contact Us</a>
    </nav>
  </div>
</header>

<section class="hero">
  <h1>At Halvern Crest Insurance, we understand<br>that your peace of mind is invaluable.</h1>
  <p>Our mission is to protect what matters most to you—your home, your vehicle, your health, and your loved ones. With our comprehensive range of insurance solutions, we are dedicated to safeguarding your assets and providing you with the security you deserve.</p>

  <div class="hero-cards">
    <div class="hcard navy">
      <div class="ring"><div role="img" aria-label="Hands holding a small model house surrounded by insurance icons" style="background:linear-gradient(135deg,#b9c8d8,#c24a3a 60%,#6a7e92)"></div></div>
      <div style="text-align:left">
        <h3>Property Insurance</h3>
        <p>Lorem ipsum dolor sit amet, consectetur adipiscing elit, sed do eiusmod dolore aliqua.</p>
        <a class="pill btn-green" href="#">Find Property Insurance
          <svg width="16" height="12" viewBox="0 0 16 12"><path d="M0 6h14M9 1l5 5-5 5" stroke="#fff" stroke-width="2" fill="none"/></svg></a>
      </div>
    </div>
    <div class="hcard green">
      <div class="ring"><div role="img" aria-label="Hand holding an umbrella over small figures of a family" style="background:linear-gradient(135deg,#3a2a1e,#b77a3e 55%,#2a1c12)"></div></div>
      <div style="text-align:left">
        <h3>Business Insurance</h3>
        <p>Lorem ipsum dolor sit amet, consectetur adipiscing elit, sed do eiusmod dolore aliqua.</p>
        <a class="pill btn-navy" href="#">Find Property Insurance
          <svg width="16" height="12" viewBox="0 0 16 12"><path d="M0 6h14M9 1l5 5-5 5" stroke="#fff" stroke-width="2" fill="none"/></svg></a>
      </div>
    </div>
  </div>

  <div class="strip">Independent insurance agents work with these insurance companies and more. <u>See the best insurance companies near you</u>
    <svg width="16" height="16" viewBox="0 0 16 16"><circle cx="8" cy="8" r="8" fill="#fff"/><path d="M4 8h7M8 5l3 3-3 3" stroke="#07206e" stroke-width="2" fill="none"/></svg>
  </div>
</section>

<section class="partners">
  <svg class="arrow" style="left:52px" width="14" height="24" viewBox="0 0 14 24"><path d="M12 2 2 12l10 10" stroke="#222" stroke-width="2" fill="none"/></svg>
  <div class="row">
    <span>Corvalith</span>
    <span>Meridale Union</span>
    <span>Tarvix</span>
    <span>Brookwynd</span>
    <span>QZT</span>
  </div>
  <svg class="arrow" style="right:52px" width="14" height="24" viewBox="0 0 14 24"><path d="M2 2l10 10L2 22" stroke="#222" stroke-width="2" fill="none"/></svg>
</section>

<section class="about">
  <div class="wrap">
    <div class="about-text">
      <h2 class="title">About <span>Us</span></h2>
      <p>Halvern Crest Insurance is a full-service, independent insurance agency with over three decades of experience in delivering comprehensive insurance solutions to individuals.</p>
      <p>We proudly offer a diverse portfolio of products from <b>more than 20</b> of the most reputable and financially secure companies in the industry. Our dedicated team of over <b>50 skilled professionals</b> is committed to customizing these products and services to meet the unique needs of each client.</p>
      <a class="btn btn-navy" href="#">Read More</a>
    </div>
    <div class="about-figure">
      <div class="back"></div>
      <div class="frame"></div>
      <div class="photo" role="img" aria-label="Family sitting on a living room floor under a cardboard roof"></div>
    </div>
  </div>
</section>

<section class="info">
  <h2>Looking for insurance <span>information?</span></h2>
  <p class="sub">Buy insurance smarter with these insurance buying tips</p>
  <div class="cards">
    <div class="card g">
      <div class="img" role="img" aria-label="Hands sheltering a model house, car and family figures" style="background:linear-gradient(135deg,#3d4550,#b8bcc4 55%,#4b5562)"></div>
      <h3>Does My Car Insurance Cover Scratches?</h3>
      <p>At Halvern Crest Insurance, our experts are focused on addressing the individual needs of our clients, ensuring exceptional service and support at every step.</p>
      <a class="more" href="#">Read the full story ➔</a>
    </div>
    <div class="card n">
      <div class="img" role="img" aria-label="Couple meeting with an agent at an office desk" style="background:linear-gradient(135deg,#2a3440,#c9cdd2 50%,#8a9aa6)"></div>
      <h3>What Insurance Do I Need to Start a<br>Business?</h3>
      <p>At Halvern Crest Insurance, our experts are focused on exceptional service and support at every step.</p>
      <a class="more" href="#">Read the full story ➔</a>
    </div>
  </div>
  <a class="blog-link" href="#">Get more tips in our insurance blog
    <svg width="16" height="16" viewBox="0 0 16 16" style="vertical-align:-2px;margin-left:6px"><circle cx="8" cy="8" r="7" fill="none" stroke="#6a9a35" stroke-width="2"/><path d="M5 8h5M8 5.5 10.5 8 8 10.5" stroke="#6a9a35" stroke-width="2" fill="none"/></svg></a>
</section>

<section class="quote">
  <div class="wrap">
    <div class="quote-form">
      <h3>Just some basic information. The address of your personal property will help in finding the right local agent for you.</h3>
      <label>Enter the address of your insurable property</label>
      <div class="field"><div class="ico"><svg width="16" height="16" viewBox="0 0 16 16"><circle cx="6.5" cy="6.5" r="5" stroke="#222" stroke-width="2.2" fill="none"/><path d="M10 10l5 5" stroke="#222" stroke-width="2.4"/></svg></div><span>Start typing your street address</span></div>
      <label>Zip code (required)</label>
      <div class="field"><div class="ico"><svg width="16" height="16" viewBox="0 0 16 16"><circle cx="6.5" cy="6.5" r="5" stroke="#222" stroke-width="2.2" fill="none"/><path d="M10 10l5 5" stroke="#222" stroke-width="2.4"/></svg></div><span>ZIP code</span></div>
      <a class="btn btn-green" href="#">Next ➞</a>
    </div>
    <div class="quote-info">
      <h2 class="title">Get a <span>Quote</span></h2>
      <p>We believe that securing your home is one of the most important decisions you can make. Obtaining a comprehensive insurance quote is essential to understanding your coverage options and ensuring that your property is adequately protected against unforeseen events.Our team of experienced professionals is here to guide you through the process, helping you find the right policy that meets your specific needs and budget. Don't leave your home's safety to chance—get a quote today and take the first step towards peace of mind.</p>
      <a class="btn btn-navy" href="#">Get My Quote Now</a>
    </div>
  </div>
</section>

<footer class="footer">
  <div class="cols">
    <div style="width:178px">
      <h4>Quick Links</h4>
      <ul>
        <li>➔ Home</li><li>➔ About Us</li><li>➔ Get a Quote</li><li>➔ Contact Us</li>
      </ul>
    </div>
    <div style="width:210px">
      <h4>Other Links</h4>
      <ul>
        <li>➔ FAQ</li><li>➔ Tems of Use</li><li>➔ Privacy Policy</li><li>➔ Support Links</li><li>➔ Conditions</li>
      </ul>
    </div>
    <div style="width:315px">
      <h4>Contact Us</h4>
      <div class="contact-row"><i><svg width="12" height="16" viewBox="0 0 12 16"><path d="M6 0a6 6 0 0 0-6 6c0 4 6 10 6 10s6-6 6-10a6 6 0 0 0-6-6z" fill="#fff"/><circle cx="6" cy="6" r="2" fill="#6a9a35"/></svg></i>Company Name,United State.</div>
      <div class="contact-row"><i><svg width="16" height="12" viewBox="0 0 16 12"><rect width="16" height="12" rx="1" fill="#fff"/><path d="M0 1l8 6 8-6" stroke="#6a9a35" stroke-width="1.5" fill="none"/></svg></i>info@halverncrest.example</div>
      <div class="contact-row"><i><svg width="14" height="14" viewBox="0 0 14 14"><path d="M3 0l2.5 3.5-1.5 1.5c1 2 2.5 3.5 4.5 4.5l1.5-1.5L14 10.5 12 13C6 13 1 8 1 2z" fill="#fff"/></svg></i>(555) 318-2740</div>
    </div>
    <div class="news" style="width:282px">
      <h4>Sign Up To Our Newsletter</h4>
      <p>Lorem ipsum dolor sit amet,consectetur adipiscing elit,adipiscing elit.</p>
      <div class="email">Email</div>
      <div class="sub-btn">Subscribe</div>
    </div>
  </div>
  <div class="copyright">Copyrights@2025.Halvern Crest Insurance, LP.All Rights Reserved</div>
</footer>

</body>
</html>
```